CD Cover Design Project For New Electronic Album

Hi, I need cover artwork for my forth coming electronic music album. The requirement is for the single page front insert and also the tray liner (rear inlay). You can find the required specifications here http://www.quillpressmedia.co.uk/artwork_specs.php

The title of the album is Velmorandine and the artists name is Owen Pritcham.

The theme of the album is the world and water, so that needs to play a big part in the imagery. An example of the kind of thing I'm looking for can be found at

http://www.brackenimagery.com/media/482736/view (this image is copyrighted, so please don't use for your own work).

I have no preference for the rear inlay, so please feel free to come up with something, so long as it is in keeping with the design for the front. There needs to be room for the song titles though, but not sure how many yet!

Good luck!
Updates

If you would like to hear a small section of the type of music to be on the album, you can listen at my tunewharf account.

https://tunewharf.com/copper-lantern/sets/velmorandine

This also contains a mock up of an album cover that was originally thought of, however permission could not be gained for the use of the image.

Industry/Entity Type

Electronic

```html
<!DOCTYPE html>
<html lang="en">
<head>
<meta charset="utf-8">
<title>Velmorandine – Owen Pritcham – CD Artwork</title>
<link href="https://fonts.googleapis.com/css2?family=Montserrat:wght@800&family=Questrial&display=swap" rel="stylesheet">
<style>
  :root {
    --stage-light: #f2f2f2;
    --stage-mid: #c9c9c9;
    --ink-black: #000000;
    --ink-white: #f4f4f4;
    --ocean-deep: #0d2a44;
    --ocean-blue: #2f6f9e;
    --ocean-glow: #5fb3e6;
    --land-green: #6e8a3c;
    --water-teal: #2a4f57;
    --spine-blue: #3f86b8;
    --spine-grey: #d8d8d8;
    --spine-dark: #1c1c1c;
    --track-text: #e2e2e2;
  }
  * { margin: 0; padding: 0; box-sizing: border-box; }
  html, body { width: 763px; height: 1200px; overflow: hidden; }
  body {
    position: relative;
    background: linear-gradient(90deg, var(--stage-mid) 0%, var(--stage-light) 50%, var(--stage-mid) 100%);
    font-family: "Questrial", "Century Gothic", sans-serif;
  }

  /* Front insert */
  .front-insert {
    position: absolute; left: 86px; top: 11px; width: 589px; height: 585px;
    background: var(--ink-black); overflow: hidden;
  }
  .front-artwork {
    position: absolute; left: 30px; top: -20px; width: 534px; height: 534px; border-radius: 50%;
    background:
      radial-gradient(circle at 50% 50%, var(--land-green) 0%, var(--ocean-blue) 18%, var(--ocean-deep) 24%, transparent 26%),
      radial-gradient(circle at 50% 50%, transparent 34%, var(--water-teal) 45%, rgba(42,79,87,0.4) 60%, transparent 70%);
  }
  .album-title { position: absolute; left: 21px; top: 438px; width: 548px; height: 70px; }
  .album-title text {
    font-family: "Montserrat", "Arial Black", sans-serif; font-weight: 800;
    font-size: 66px; fill: var(--ink-white);
  }
  .artist-name {
    position: absolute; left: 21px; top: 514px; width: 548px;
    display: flex; justify-content: space-between;
    font-size: 18px; color: var(--ink-white);
  }

  /* Tray liner */
  .tray-liner {
    position: absolute; left: 10px; top: 602px; width: 742px; height: 586px; overflow: hidden;
    background: linear-gradient(90deg, var(--ink-black) 0%, var(--ink-black) 78%, #3a3a3a 92%, #8a8a8a 100%);
  }
  .rear-artwork {
    position: absolute; left: 0; top: 0; width: 742px; height: 586px;
    background:
      radial-gradient(circle 70px at 450px 366px, rgba(255,255,255,0.95) 0%, rgba(255,255,255,0.35) 20%, transparent 100%),
      radial-gradient(circle 90px at 200px 180px, rgba(120,140,150,0.18) 0%, transparent 100%),
      radial-gradient(circle 218px at 668px 312px, var(--ocean-glow) 0%, var(--ocean-blue) 60%, var(--ocean-deep) 99%, transparent 100%);
  }
  .spine-label {
    position: absolute; font-size: 14px; letter-spacing: 0.5px; white-space: nowrap;
    display: flex; align-items: center; gap: 10px;
  }
  .spine-label .artist { color: var(--spine-grey); }
  .spine-label .title { color: var(--spine-blue); }
  .spine-label .dot {
    width: 8px; height: 8px; border-radius: 50%; border: 1px solid var(--spine-blue);
  }
  .spine-left { left: 28px; top: 298px; transform-origin: 0 0; transform: rotate(-90deg); }
  .spine-right { left: 722px; top: 58px; transform-origin: 0 0; transform: rotate(90deg); }
  .spine-right .artist { color: var(--spine-dark); }

  .track-list {
    position: absolute; left: 106px; top: 326px; list-style: none;
    font-size: 13px; line-height: 20px; color: var(--track-text);
  }
</style>
</head>
<body>
  <section class="front-insert">
    <div class="front-artwork" role="img" aria-label="Earth globe surrounded by a ring of splashing water on black"></div>
    <svg class="album-title" viewBox="0 0 548 70">
      <text x="0" y="62" textLength="548" lengthAdjust="spacingAndGlyphs">VELMORANDINE</text>
    </svg>
    <div class="artist-name">
      <span>O</span><span>W</span><span>E</span><span>N</span><span>&nbsp;</span><span>P</span><span>R</span><span>I</span><span>T</span><span>C</span><span>H</span><span>A</span><span>M</span>
    </div>
  </section>

  <section class="tray-liner">
    <div class="rear-artwork" role="img" aria-label="Blue relief globe lit from the left by a bright lens flare in dark space"></div>
    <div class="spine-label spine-left"><span class="artist">OWEN PRITCHAM</span><span class="dot"></span><span class="title">VELMORANDINE</span></div>
    <div class="spine-label spine-right"><span class="artist">OWEN PRITCHAM</span><span class="dot"></span><span class="title">VELMORANDINE</span></div>
    <ol class="track-list">
      <li>1. Beneath The Tide &amp; Velmorandine Part 1</li>
      <li>2. Swell</li>
      <li>3. The Drift</li>
      <li>4. Undertow - Sketch &amp; Sound Check</li>
      <li>5. Echoes Of The Shallows</li>
      <li>6. Draft Album Mix</li>
      <li>7. ...</li>
      <li>8. ...</li>
      <li>9. ...</li>
    </ol>
  </section>
</body>
</html>
```